Graduation backdrop sign

I need a sign that says
Hey look ma...we made it!.
I want the Hey look ma on one line and in a more blocky font and then the other line of we made it in a more feminine font but something you can read. I am planning to send this file to a printing place to make an acrylic sign. The backdrop color is a bright pink, fuscia and orange colors with gold accent so I am thinking of the background being white with a cute scallop border or a cloud like border. Then make the colors of the fonts be a bright dark pink with orange and gold accents somehow. and maybe a cute but no overwhelming border or accents around the font to make it bright and cheery. I am attaching the backdrop that this will be hung in.

```html
<!DOCTYPE html>
<html lang="en">
<head>
<meta charset="utf-8">
<title>Hey look ma... we made it!</title>
<link rel="stylesheet" href="https://fonts.googleapis.com/css2?family=Playfair+Display:wght@700&display=swap">
<style>
  :root {
    --scallop: #f47a78;
    --gold: #f4bf0a;
    --orange: #fa5e17;
    --paper: #ffffff;
    --fuchsia: #be1c82;
    --blush: #fcedef;
  }
  html, body {
    margin: 0;
    padding: 0;
    width: 900px;
    height: 1200px;
    overflow: hidden;
    background: var(--paper);
  }
  .sign {
    display: block;
    width: 900px;
    height: 1200px;
  }
  .scallop-border { fill: var(--scallop); }
  .frame-white { fill: var(--paper); }
  .frame-gold { fill: var(--gold); }
  .frame-orange { fill: var(--orange); }
  .panel { fill: var(--paper); }
  .headline {
    font-family: "Playfair Display", Georgia, serif;
    font-weight: 700;
    fill: var(--fuchsia);
    stroke: var(--blush);
    stroke-width: 26px;
    stroke-linejoin: round;
    paint-order: stroke fill;
    text-anchor: middle;
  }
</style>
</head>
<body>
<svg class="sign" viewBox="0 0 900 1200" xmlns="http://www.w3.org/2000/svg" role="img" aria-label="Hey look ma... we made it!.">
  <defs>
    <circle id="bump-h" r="34"/>
    <circle id="bump-v" r="44"/>
  </defs>

  <g class="scallop-border">
    <rect x="30" y="30" width="840" height="1140"/>
    <!-- top and bottom bumps -->
    <g>
      <use href="#bump-h" x="52" y="38"/><use href="#bump-h" x="118" y="38"/><use href="#bump-h" x="184" y="38"/>
      <use href="#bump-h" x="250" y="38"/><use href="#bump-h" x="316" y="38"/><use href="#bump-h" x="382" y="38"/>
      <use href="#bump-h" x="450" y="38"/><use href="#bump-h" x="518" y="38"/><use href="#bump-h" x="584" y="38"/>
      <use href="#bump-h" x="650" y="38"/><use href="#bump-h" x="716" y="38"/><use href="#bump-h" x="782" y="38"/>
      <use href="#bump-h" x="848" y="38"/>
      <use href="#bump-h" x="52" y="1162"/><use href="#bump-h" x="118" y="1162"/><use href="#bump-h" x="184" y="1162"/>
      <use href="#bump-h" x="250" y="1162"/><use href="#bump-h" x="316" y="1162"/><use href="#bump-h" x="382" y="1162"/>
      <use href="#bump-h" x="450" y="1162"/><use href="#bump-h" x="518" y="1162"/><use href="#bump-h" x="584" y="1162"/>
      <use href="#bump-h" x="650" y="1162"/><use href="#bump-h" x="716" y="1162"/><use href="#bump-h" x="782" y="1162"/>
      <use href="#bump-h" x="848" y="1162"/>
    </g>
    <!-- left and right bumps -->
    <g>
      <use href="#bump-v" x="48" y="70"/><use href="#bump-v" x="48" y="162"/><use href="#bump-v" x="48" y="254"/>
      <use href="#bump-v" x="48" y="346"/><use href="#bump-v" x="48" y="438"/><use href="#bump-v" x="48" y="530"/>
      <use href="#bump-v" x="48" y="622"/><use href="#bump-v" x="48" y="714"/><use href="#bump-v" x="48" y="806"/>
      <use href="#bump-v" x="48" y="898"/><use href="#bump-v" x="48" y="990"/><use href="#bump-v" x="48" y="1082"/>
      <use href="#bump-v" x="852" y="70"/><use href="#bump-v" x="852" y="162"/><use href="#bump-v" x="852" y="254"/>
      <use href="#bump-v" x="852" y="346"/><use href="#bump-v" x="852" y="438"/><use href="#bump-v" x="852" y="530"/>
      <use href="#bump-v" x="852" y="622"/><use href="#bump-v" x="852" y="714"/><use href="#bump-v" x="852" y="806"/>
      <use href="#bump-v" x="852" y="898"/><use href="#bump-v" x="852" y="990"/><use href="#bump-v" x="852" y="1082"/>
    </g>
  </g>

  <rect class="frame-white" x="58" y="57" width="784" height="1081" rx="6"/>
  <rect class="frame-gold" x="64" y="63" width="770" height="1068"/>
  <rect class="frame-orange" x="84" y="82" width="729" height="1033" rx="4"/>
  <rect class="panel" x="95" y="93" width="707" height="1011"/>

  <g class="headline">
    <text x="453" y="354" font-size="134" textLength="492" lengthAdjust="spacingAndGlyphs">Hey look</text>
    <text x="487" y="485" font-size="134" textLength="250" lengthAdjust="spacingAndGlyphs">ma...</text>
    <text x="450" y="643" font-size="134" textLength="460" lengthAdjust="spacingAndGlyphs">we made</text>
    <text x="456" y="795" font-size="134" textLength="128" lengthAdjust="spacingAndGlyphs">it!.</text>
  </g>
</svg>
</body>
</html>
```